WebApp for IoT (Vex lights and Tarvo/Brindle)

I am going to create my own dashbord for Caskel Pro (See other examples on https://caskel.example/) But I want it much more flexible and advanced.
One page per room (So I can have an Tabro in each room with all functions just for that room) and include controls for light (both overall for the room and in an popupwindow all lightbulbs n the room - se more about how its done in Gorvan Vex app on https://www.gorvan-vex.example/en-us/explore-vex/apps/bridge) aswell as set volume/track for Tarvo.

I want the final solution to be "skinable" so I can choose from Blue-CSS to Green-CSS etc, but at this moment I only want ONE color!

I have added an PDF with the functions I am thinking of, but the design is for you to create!

Please have in mind it will be running on Tabros on the wall, and in the mobile.

For the moment I only want an PSD of the "Room page", "Light popup" and "Sound Popup", but I might contract the winner to get HTML/CSS as second step.

```html
<!DOCTYPE html>
<html lang="en">
<head>
<meta charset="utf-8">
<title>Room Dashboard</title>
<link href="https://fonts.googleapis.com/css2?family=Poppins:wght@500;600;700&display=swap" rel="stylesheet">
<style>
  :root {
    --screen-bg: #d8d9da;
    --screen-glow: #e6e7e8;
    --card-bg: #cacbcd;
    --ink: #1f1f21;
    --ink-soft: #3a3b3d;
    --rule: #b7b8ba;
    --icon-circle: #c9cacc;
    --toggle-track: #b4b5b8;
    --toggle-knob: #f2f2f2;
    --star: #d9952c;
    --pill-border: #c2c3c5;
    --play-bg: #2a2b2d;
    --sun: #f1c21b;
    --cloud: #b9dbe8;
  }
  * { margin: 0; padding: 0; box-sizing: border-box; }
  html, body { width: 1200px; height: 962px; overflow: hidden; }
  body {
    font-family: "Poppins", sans-serif;
    color: var(--ink);
    background: radial-gradient(ellipse at 40% 30%, var(--screen-glow) 0%, var(--screen-bg) 70%);
    position: relative;
  }
  .room-page { position: absolute; inset: 0; }

  /* Header */
  .room-badge {
    position: absolute; left: 43px; top: 101px;
    width: 84px; height: 84px; border-radius: 50%;
    background: var(--icon-circle);
    display: flex; align-items: center; justify-content: center;
  }
  .room-title {
    position: absolute; left: 145px; top: 108px;
    font-size: 52px; font-weight: 700; letter-spacing: 0.5px; line-height: 1;
  }
  .weather-icon { position: absolute; left: 498px; top: 88px; }
  .weather-temp {
    position: absolute; left: 613px; top: 84px;
    font-size: 52px; font-weight: 500; line-height: 1;
  }
  .weather-temp sup { font-size: 34px; font-weight: 500; vertical-align: 16px; }
  .weather-desc {
    position: absolute; left: 614px; top: 138px;
    font-size: 27px; font-weight: 500; line-height: 1;
  }
  .clock-icon { position: absolute; left: 966px; top: 133px; }
  .datetime {
    position: absolute; left: 1029px; top: 128px;
    font-size: 21px; font-weight: 600; line-height: 1.35;
  }
  .header-rule {
    position: absolute; left: 43px; top: 254px; width: 1113px; height: 1px;
    background: var(--rule);
  }

  /* Favourite cards */
  .favorite-star { position: absolute; left: 121px; }
  .control-card {
    position: absolute; left: 173px; width: 477px; height: 127px;
    background: var(--card-bg); border-radius: 12px;
    display: flex; align-items: center; padding-left: 30px;
  }
  .control-card .card-icon { width: 52px; height: 52px; flex: none; }
  .control-card .card-label {
    margin-left: 15px; font-size: 30px; font-weight: 500; color: var(--ink-soft);
  }
  .toggle {
    position: absolute; left: 373px; top: 43px;
    width: 73px; height: 40px; border-radius: 20px;
    background: var(--toggle-track);
  }
  .toggle::after {
    content: ""; position: absolute; right: 6px; top: 6px;
    width: 28px; height: 28px; border-radius: 50%; background: var(--toggle-knob);
  }
  .column-rule {
    position: absolute; left: 779px; top: 343px; width: 1px; height: 352px;
    background: var(--rule);
  }

  /* Flows */
  .flow-button {
    position: absolute; left: 888px; width: 188px; height: 70px;
    border: 2px solid var(--pill-border); border-radius: 35px;
    display: flex; align-items: center; padding-left: 9px;
    font-size: 25px; font-weight: 500; color: var(--ink);
  }
  .flow-button .play {
    width: 52px; height: 52px; border-radius: 50%; background: var(--play-bg);
    display: flex; align-items: center; justify-content: center; margin-right: 16px; flex: none;
  }
</style>
</head>
<body>
<main class="room-page">
  <header>
    <div class="room-badge">
      <svg width="46" height="34" viewBox="0 0 46 34" fill="none" stroke="#2a2b2d" stroke-width="2.6" stroke-linejoin="round">
        <rect x="5" y="3" width="36" height="14" rx="3"/>
        <rect x="10" y="9" width="11" height="8" rx="2"/>
        <rect x="25" y="9" width="11" height="8" rx="2"/>
        <rect x="2" y="17" width="42" height="10" rx="2"/>
        <line x1="6" y1="27" x2="6" y2="32"/>
        <line x1="40" y1="27" x2="40" y2="32"/>
      </svg>
    </div>
    <h1 class="room-title">ROOM</h1>

    <svg class="weather-icon" width="98" height="84" viewBox="0 0 98 84" role="img" aria-label="Sun partly behind a cloud">
      <g stroke="var(--sun)" stroke-width="2.5" stroke-linecap="round">
        <line x1="62" y1="2" x2="62" y2="10"/>
        <line x1="84" y1="10" x2="79" y2="16"/>
        <line x1="93" y1="32" x2="85" y2="32"/>
        <line x1="40" y1="10" x2="45" y2="16"/>
        <line x1="84" y1="54" x2="79" y2="48"/>
      </g>
      <circle cx="62" cy="32" r="19" fill="var(--sun)"/>
      <path d="M12 80 h60 a14 14 0 0 0 2 -28 a20 20 0 0 0 -38 -6 a15 15 0 0 0 -22 12 a11 11 0 0 0 -2 22 z" fill="var(--cloud)"/>
    </svg>
    <div class="weather-temp">23<sup>°C</sup></div>
    <div class="weather-desc">Sunny</div>

    <svg class="clock-icon" width="48" height="48" viewBox="0 0 48 48" fill="none" stroke="#2a2b2d" stroke-width="2.4" stroke-linecap="round">
      <circle cx="24" cy="24" r="21"/>
      <polyline points="24,11 24,24 31,31"/>
    </svg>
    <div class="datetime">2022-07-14<br>15:23</div>
  </header>

  <div class="header-rule"></div>

  <section class="favorites">
    <svg class="favorite-star" style="top:342px" width="30" height="30" viewBox="0 0 24 24"><path d="M12 1.5l3 7 7.5.6-5.7 5 1.8 7.4L12 17.6 5.4 21.5l1.8-7.4-5.7-5 7.5-.6z" fill="var(--star)"/></svg>
    <div class="control-card" style="top:343px">
      <svg class="card-icon" viewBox="0 0 52 52" fill="none" stroke="#2a2b2d" stroke-width="2.4" stroke-linecap="round">
        <line x1="26" y1="3" x2="26" y2="10"/>
        <path d="M8 28 a18 17 0 0 1 36 0 z" stroke-linejoin="round"/>
        <path d="M20 28 a6 6 0 0 0 12 0"/>
        <line x1="26" y1="39" x2="26" y2="47"/>
        <line x1="15" y1="36" x2="10" y2="42"/>
        <line x1="37" y1="36" x2="42" y2="42"/>
      </svg>
      <span class="card-label">Light Details</span>
      <span class="toggle" aria-label="Light toggle"></span>
    </div>

    <svg class="favorite-star" style="top:495px" width="30" height="30" viewBox="0 0 24 24"><path d="M12 1.5l3 7 7.5.6-5.7 5 1.8 7.4L12 17.6 5.4 21.5l1.8-7.4-5.7-5 7.5-.6z" fill="var(--star)"/></svg>
    <div class="control-card" style="top:496px">
      <svg class="card-icon" viewBox="0 0 52 52" fill="none" stroke="#2a2b2d" stroke-width="2.4" stroke-linecap="round" stroke-linejoin="round">
        <path d="M4 19 h8 l12 -10 v34 l-12 -10 h-8 z"/>
        <line x1="12" y1="19" x2="12" y2="33"/>
        <path d="M31 19 a9 9 0 0 1 0 14"/>
        <path d="M36 14 a15 15 0 0 1 0 24"/>
        <path d="M41 9 a21 21 0 0 1 0 34"/>
      </svg>
      <span class="card-label">Sound Details</span>
      <span class="toggle" aria-label="Sound toggle"></span>
    </div>
  </section>

  <div class="column-rule"></div>

  <nav class="flows">
    <div class="flow-button" style="top:358px"><span class="play"><svg width="14" height="16" viewBox="0 0 14 16"><path d="M2 1l11 7-11 7z" fill="#fff"/></svg></span>Flow 1</div>
    <div class="flow-button" style="top:453px"><span class="play"><svg width="14" height="16" viewBox="0 0 14 16"><path d="M2 1l11 7-11 7z" fill="#fff"/></svg></span>Flow 2</div>
    <div class="flow-button" style="top:548px"><span class="play"><svg width="14" height="16" viewBox="0 0 14 16"><path d="M2 1l11 7-11 7z" fill="#fff"/></svg></span>Flow 3</div>
    <div class="flow-button" style="top:642px"><span class="play"><svg width="14" height="16" viewBox="0 0 14 16"><path d="M2 1l11 7-11 7z" fill="#fff"/></svg></span>Flow 4</div>
  </nav>
</main>
</body>
</html>
```